Trifold - Birch Commercial Roofing

Enhance the look, change the images if needed. Create some interest please!

Target Market(s)

Commercial and Industrial Building Owners

Industry/Entity Type

Roofing

Font styles to use
Serif

Requirements
Must have
• Organized layout, call to action

```html
<!DOCTYPE html>
<html lang="en">
<head>
<meta charset="utf-8">
<title>Birch Commercial Roofing – Trifold</title>
<link href="https://fonts.googleapis.com/css2?family=Tinos:wght@400;700&family=PT+Sans:wght@400&display=swap" rel="stylesheet">
<style>
:root{
  --stage:#5e5e5e;
  --ink:#111111;
  --black:#0c0c0c;
  --paper:#f4f4f4;
  --paper-shade:#dcdcdc;
  --silver:#b9b9b9;
  --white:#ffffff;
  --smoke:#3a3a3a;
  --flame:#d9703a;
}
*{margin:0;padding:0;box-sizing:border-box}
html,body{width:1200px;height:3600px;overflow:hidden;background:var(--stage)}
body{position:relative;font-family:"PT Sans",Arial,sans-serif;color:var(--ink)}
.spread{position:absolute;left:60px;width:1080px;height:764px;overflow:hidden;
  background:linear-gradient(90deg,var(--paper) 0%,#ffffff 30%,var(--paper-shade) 33.3%,#ffffff 36%,var(--paper) 64%,var(--paper-shade) 66.6%,#ffffff 69%,var(--paper) 100%);
  box-shadow:0 20px 40px rgba(0,0,0,.45)}
.spread--outside{top:518px}
.spread--inside{top:2318px}
.shapes{position:absolute;inset:0;width:100%;height:100%}
.block{position:absolute;text-align:center}
.heading{font-family:"Tinos","Times New Roman",serif;font-weight:400;color:var(--ink);line-height:1.1}
.heading--lg{font-size:29px;letter-spacing:.5px}
.heading--md{font-size:23px}
.copy{font-size:11.4px;line-height:1.38;text-align:justify;text-align-last:center;margin-top:10px}
.brand{position:absolute;font-family:"Tinos","Times New Roman",serif;font-weight:400;color:var(--ink);
  letter-spacing:5px;text-transform:uppercase;display:flex;align-items:center;gap:10px;white-space:nowrap}
.brand::before{content:"";width:12px;height:12px;border-radius:50%;background:var(--ink)}
.title{position:absolute;font-family:"Tinos","Times New Roman",serif;color:var(--white);text-align:center;line-height:1.05}
.title .t1,.title .t3{font-size:34px}
.title .t2{font-size:44px;font-weight:700;letter-spacing:1px}
.contact{position:absolute;text-align:center}
.contact .phone{font-family:"Tinos","Times New Roman",serif;font-size:33px}
.contact .addr{font-size:11px;margin-top:6px}
.contact .web{font-size:12px;letter-spacing:3px;margin-top:18px}
</style>
</head>
<body>

<section class="spread spread--outside" aria-label="Trifold outside">
  <svg class="shapes" viewBox="0 0 1080 764" xmlns="http://www.w3.org/2000/svg">
    <defs>
      <linearGradient id="cityFade" x1="0" y1="0" x2="0" y2="1">
        <stop offset="0" stop-color="#e6e6e6" stop-opacity="0"/>
        <stop offset="1" stop-color="#cfcfcf" stop-opacity=".9"/>
      </linearGradient>
      <linearGradient id="hospital" x1="0" y1="0" x2="0" y2="1">
        <stop offset="0" stop-color="#c9d8e8"/>
        <stop offset=".45" stop-color="#d8d6d0"/>
        <stop offset=".75" stop-color="#7f8a72"/>
        <stop offset="1" stop-color="#5d6b4c"/>
      </linearGradient>
      <linearGradient id="campus" x1="0" y1="0" x2="1" y2="1">
        <stop offset="0" stop-color="#8fb6e0"/>
        <stop offset=".55" stop-color="#a4584a"/>
        <stop offset="1" stop-color="#c9c2b4"/>
      </linearGradient>
    </defs>
    <rect x="280" y="330" width="420" height="434" fill="url(#cityFade)" role="img" aria-label="Faint city skyline photograph"/>
    <path d="M560 0 L1080 0 L1080 720 Q760 700 610 520 Q520 400 560 0 Z" fill="var(--silver)"/>
    <path d="M575 0 L1080 0 L1080 705 Q770 690 625 515 Q535 400 575 0 Z" fill="var(--black)"/>
    <circle cx="790" cy="200" r="300" fill="url(#hospital)" role="img" aria-label="Aerial photograph of a hospital campus with flat roofs"/>
    <path d="M0 505 Q260 470 450 764 L0 764 Z" fill="var(--black)"/>
    <path d="M0 545 Q240 520 400 764 L0 764 Z" fill="url(#campus)" role="img" aria-label="Photograph of a brick commercial building"/>
  </svg>

  <div class="block" style="left:34px;top:58px;width:300px">
    <h2 class="heading heading--lg">WHO WE ARE</h2>
    <p class="copy">Birch Commercial is a flat roof and specialty roofing woman-owned business servicing the Chicagoland area. With more than 16 years of experience in roofing and construction it is our goal to share our industry knowledge and expertise to build and maintain the systems that cover your assets.</p>
    <p class="copy">We strive to devise the best roofing solution for your requirements and budget. Clients receive the utmost attention to detail in understanding the work scope and expectations of a project from beginning to end. We are committed to quality installation processes and providing safe work environments for our skilled tradesmen and women.</p>
  </div>
  <div class="block" style="left:34px;top:358px;width:300px">
    <h2 class="heading heading--lg">ROOF ASSESSMENT</h2>
    <p class="copy">What is the condition of your roof? Our roof evaluation will offer you insight to determine whether you should simply implement routine maintenance or if the roof is due for repairs, overlay or a full replacement.</p>
  </div>

  <div class="brand" style="right:34px;top:52px;font-size:22px">Birch Commercial</div>

  <div class="title" style="right:40px;top:530px;width:280px">
    <div class="t1">Birch Commercial</div>
    <div class="t2">ROOFING</div>
    <div class="t3">Construction</div>
  </div>

  <div class="contact" style="left:395px;top:620px;width:280px">
    <div class="phone">(312) 555-0148</div>
    <div class="addr">4180 Alder Lane, Suite B, Maple Ridge, IL 60999</div>
    <div class="web">www.birchroof.com</div>
  </div>
</section>

<section class="spread spread--inside" aria-label="Trifold inside">
  <svg class="shapes" viewBox="0 0 1080 764" xmlns="http://www.w3.org/2000/svg">
    <defs>
      <linearGradient id="arena" x1="0" y1="0" x2="0" y2="1">
        <stop offset="0" stop-color="#5f7f4e"/>
        <stop offset=".35" stop-color="#b0583f"/>
        <stop offset=".65" stop-color="#c8b89c"/>
        <stop offset="1" stop-color="#8a8d90"/>
      </linearGradient>
      <radialGradient id="fire" cx=".4" cy=".4" r=".7">
        <stop offset="0" stop-color="var(--flame)"/>
        <stop offset=".35" stop-color="var(--smoke)"/>
        <stop offset=".8" stop-color="#6b7a8c"/>
        <stop offset="1" stop-color="#4f6a3e"/>
      </radialGradient>
    </defs>
    <path d="M0 0 L780 0 Q760 300 500 360 Q300 395 0 330 Z" fill="var(--silver)"/>
    <path d="M0 0 L770 0 Q745 290 495 345 Q300 385 0 315 Z" fill="var(--black)"/>
    <path d="M75 0 L760 0 Q740 250 480 300 Q240 330 75 0 Z" fill="url(#arena)" role="img" aria-label="Aerial photograph of an arena with a large flat roof"/>
    <path d="M1080 450 Q800 450 700 764 L1080 764 Z" fill="var(--silver)"/>
    <path d="M1080 465 Q815 470 715 764 L1080 764 Z" fill="var(--black)"/>
    <path d="M1080 495 Q850 500 755 764 L1080 764 Z" fill="url(#fire)" role="img" aria-label="Aerial photograph of firefighters spraying a burning commercial building"/>
  </svg>

  <div class="brand" style="left:775px;top:96px;font-size:19px">Birch Commercial</div>

  <div class="block" style="left:755px;top:188px;width:300px">
    <h3 class="heading heading--md">Preventative Maintenance</h3>
    <p class="copy">We service your roof to keep you dry and aware of any issues we foresee. See below for preventive packages and ask us to assist you in selecting what fits best. We offer three distinct packages to cover every type of roof.</p>
  </div>
  <div class="block" style="left:755px;top:318px;width:300px">
    <h3 class="heading heading--md">Government + Municipal<br>Bidding</h3>
    <p class="copy">We have comprehensive experience working with municipal and government projects. Our expert team and estimating department is compliant with the state of Illinois to bid any project of any size.</p>
  </div>

  <div class="block" style="left:395px;top:385px;width:290px">
    <h3 class="heading heading--md">24/7 Emergency Repairs</h3>
    <p class="copy">You can't plan for an emergency, which is why our 24/7 servicers are ready to assist! We offer a full range of roofing services, from minor repairs to complete replacements. We understand the need to get your roof restored as quickly as possible. Our emergency repair service is just a phone call away.</p>
  </div>
  <div class="block" style="left:395px;top:548px;width:290px">
    <h3 class="heading heading--md">Architectural Drawings +<br>Engineering</h3>
    <p class="copy">Have a new property build that needs to comply with strict guidelines and restrictions? We offer architectural drawings from engineers who can certify your property to meet any and all guidelines and code compliance.</p>
  </div>

  <div class="block" style="left:30px;top:410px;width:300px">
    <h2 class="heading heading--lg" style="font-size:27px">SERVICES</h2>
    <h3 class="heading heading--md" style="margin-top:14px">Roof Assessment</h3>
    <p class="copy">What is the condition of your roof? Our roof evaluation will offer you insight to determine whether you should simply implement routine maintenance or if the roof is due for repairs, overlay or a full replacement.</p>
    <h3 class="heading heading--md" style="margin-top:20px">Insurance Restoration</h3>
    <p class="copy">Was your property involved in an accident or natural disaster that caused mold, mildew, fire, hail or water damage? Birch Commercial works directly with your insurance company restore your property as efficiently as possible. We can repair or rebuild any size structure, ensuring a safe and comfortable place for your business.</p>
  </div>
</section>

</body>
</html>
```